Property management company looking for modern card design

We at Blue Maple Holdings provides property management services for its residential and commercial properties, with expertise in all categories of multifamily, industrial and office projects throughout California.

We need a business card design that is professional and modern designed business card. In our field, clients get hundreds of business cards, we would like our card to stand out.

Please avoid small print.

Target Market(s)

Professionals and high end clients

Industry/Entity Type

Financial Planning

Contact Information for Business Card

Company Name: Blue Maple Holdings, Name, email, license #, phone number, website bluemapleholdings.example

Font styles to use
Sans Serif

Requirements
Must have
• The card design needs to be adaptable because there is a possibly we will be expanding into different sectors other than real estate. The card design should be focused on financial planning and asset management.
Nice to have
• Modern and simple business card. Eye catching. Non-standard size/shaped cards would be great.
• bluemapleholdings.example
Should not have
• Too many bright color or any pictures or shapes of real estate stuff.

```html
<!DOCTYPE html>
<html lang="en">
<head>
<meta charset="utf-8">
<title>Blue Maple Holdings – Business Card</title>
<link rel="stylesheet" href="https://fonts.googleapis.com/css2?family=Open+Sans:wght@300;400;600;700&display=swap">
<style>
  :root {
    --backdrop: #ececec;
    --gold-light: #dcb990;
    --gold-mid: #c9a075;
    --gold-dark: #b48a5f;
    --ink: #2a2a2a;
    --card-dark: #2a2a2a;
    --gold-text: #d2a97c;
  }
  * { margin: 0; padding: 0; box-sizing: border-box; }
  html, body {
    width: 1200px; height: 900px; overflow: hidden;
    background: var(--backdrop);
    font-family: "Open Sans", Arial, sans-serif;
  }
  .canvas { position: relative; width: 1200px; height: 900px; }
  .card {
    position: absolute; top: 306px; height: 271px; border-radius: 10px; overflow: hidden;
  }
  .card-front {
    left: 149px; width: 439px;
    background: linear-gradient(135deg, var(--gold-light) 0%, var(--gold-mid) 55%, var(--gold-dark) 100%);
    color: var(--ink);
  }
  .card-back { left: 608px; width: 441px; background: var(--card-dark); }

  .brand-mark {
    position: absolute; left: 52px; top: 62px; width: 134px;
    display: flex; flex-direction: column; align-items: center; gap: 10px;
  }
  .brand-dot { width: 80px; height: 80px; border-radius: 50%; background: var(--ink); }
  .brand-name {
    font-size: 15px; font-weight: 600; line-height: 1.2; text-align: center; color: var(--ink);
  }

  .details { position: absolute; left: 232px; right: 14px; top: 70px; white-space: nowrap; }
  .person-name { font-size: 14px; font-weight: 700; line-height: 18px; }
  .person-title { font-size: 12px; font-weight: 400; line-height: 16px; }
  .license { margin-top: 20px; font-size: 12px; line-height: 18px; }
  .license strong { font-size: 13px; font-weight: 700; }
  .contact-list { list-style: none; margin-top: 9px; }
  .contact-list li {
    display: flex; align-items: center; gap: 8px;
    font-size: 11.5px; line-height: 16px;
  }
  .contact-list svg { width: 9px; height: 9px; fill: var(--ink); flex: none; }

  .wordmark {
    position: absolute; left: 0; right: 0; top: 80px;
    display: flex; flex-direction: column; align-items: center;
    color: var(--gold-text); font-weight: 300;
  }
  .wordmark-main { font-size: 53px; line-height: 60px; letter-spacing: -0.5px; }
  .wordmark-sub {
    width: 307px; display: flex; align-items: center; gap: 8px;
    font-size: 28px; line-height: 34px;
  }
  .wordmark-sub .rule { flex: 1; height: 1px; background: var(--gold-text); opacity: 0.8; }
</style>
</head>
<body>
<main class="canvas">
  <section class="card card-front">
    <div class="brand-mark">
      <span class="brand-dot"></span>
      <span class="brand-name">Blue Maple<br>Holdings</span>
    </div>
    <div class="details">
      <p class="person-name">Daniel Reyes</p>
      <p class="person-title">Managing Director</p>
      <p class="license"><strong>License:</strong> BMH01245</p>
      <ul class="contact-list">
        <li><svg viewBox="0 0 10 10"><path d="M2 0.5 L3.6 2.6 L2.6 3.8 Q3.6 5.9 6.2 7.4 L7.4 6.4 L9.5 8 L8.4 9.6 Q4.5 9.4 1.4 5.6 Q0.2 3.5 0.5 1.6 Z"/></svg>044-555 210 384</li>
        <li><svg viewBox="0 0 10 10"><path d="M0.5 2 H9.5 V8.5 H0.5 Z M0.5 2 L5 5.5 L9.5 2" fill="none" stroke="#2a2a2a" stroke-width="1"/><path d="M0.5 2 H9.5 L5 5.5 Z"/></svg>info@bluemaple.example</li>
        <li><svg viewBox="0 0 10 10"><circle cx="5" cy="5" r="4.5"/></svg>www.bluemapleholdings.example</li>
      </ul>
    </div>
  </section>

  <section class="card card-back">
    <div class="wordmark">
      <span class="wordmark-main">BLUE MAPLE</span>
      <span class="wordmark-sub"><span class="rule"></span>Holdings<span class="rule"></span></span>
    </div>
  </section>
</main>
</body>
</html>
```